Business Cards for cafe providing speciality coffee and food

I need a business card design for my husband’s businesses. He has two cafes in Brisbane. The business name is Copperleaf Roasting House. They sell high end specialty coffee as well as breakfast and lunch. All the food is cooked fresh, in house and they have strict quality controls for their coffee. I would like the business card to feature the address for both cafes, my husband’s phone number and the business’s instagram. The address for the first is 61 Wexley Crescent, Pine Hollow and the second is 23 Dorrit Avenue, Sallowmere. The Instagram handle is @copperleafroastinghouse and phone number is 0491326085. We already have a business logo that is attached.

Target Market(s)

All ages, higher disposable income and more likely to eat out regularly

Industry/Entity Type

Hospitality

Contact Information for Business Card

Must be suitable for both customers and suppliers

Font styles to use
Sans Serif

Colors

Designer to choose colors to be used in the design.

Requirements
Must have
• Owner’s name: Griff Tallant
• Addresses of both cafes: 61 Wexley Crescent, Pine Hollow and 23 Dorrit Avenue, Sallowmere
• Instagram handle: @copperleafroastinghouse
• Contact number: 0491326085
Nice to have
• Business logo

```html
<!DOCTYPE html>
<html lang="en">
<head>
<meta charset="utf-8">
<title>Copperleaf Roasting House – Business Cards</title>
<link href="https://fonts.googleapis.com/css2?family=Open+Sans:wght@400;700&display=swap" rel="stylesheet">
<style>
  :root {
    --backdrop: #2b2b2b;
    --card-black: #141414;
    --photo-light: #5a5a5a;
    --photo-mid: #3a3a3a;
    --photo-dark: #1a1a1a;
    --ink-white: #ffffff;
    --ink-soft: #e6e6e6;
  }
  * { margin: 0; padding: 0; box-sizing: border-box; }
  html, body {
    width: 1200px;
    height: 900px;
    overflow: hidden;
    background: var(--backdrop);
    font-family: "Open Sans", Arial, sans-serif;
  }
  .canvas {
    position: relative;
    width: 1200px;
    height: 900px;
  }
  .card {
    position: absolute;
    left: 290px;
    width: 620px;
    height: 350px;
    overflow: hidden;
    border-radius: 3px;
    box-shadow: 0 6px 18px rgba(0,0,0,0.45);
  }
  /* Front */
  .card-front { top: 60px; }
  .front-photo {
    position: absolute;
    inset: 0;
    background:
      radial-gradient(ellipse 40% 45% at 30% 40%, var(--photo-light) 0%, var(--photo-mid) 55%, transparent 100%),
      linear-gradient(180deg, var(--photo-mid) 0%, var(--photo-dark) 100%);
  }
  .brand-seal {
    position: absolute;
    left: 395px;
    top: 90px;
    width: 170px;
    height: 170px;
    border: 3px solid var(--ink-white);
    border-radius: 50%;
    display: flex;
    align-items: center;
    justify-content: center;
    text-align: center;
  }
  .brand-name {
    color: var(--ink-white);
    font-weight: 700;
    text-transform: uppercase;
    letter-spacing: 1px;
    line-height: 1.25;
  }
  .brand-seal .brand-name { font-size: 17px; }

  /* Back */
  .card-back {
    top: 470px;
    background: var(--card-black);
  }
  .holder-name {
    position: absolute;
    left: 40px;
    top: 40px;
    color: var(--ink-white);
    font-size: 17px;
    font-weight: 700;
    text-transform: uppercase;
  }
  .contact-list {
    position: absolute;
    left: 40px;
    top: 196px;
    list-style: none;
    color: var(--ink-soft);
    font-size: 13px;
    line-height: 1.6;
  }
  .contact-list li {
    display: flex;
    align-items: center;
    gap: 8px;
  }
  .contact-icon { width: 12px; height: 12px; flex: none; }
  .address {
    position: absolute;
    left: 40px;
    top: 258px;
    color: var(--ink-soft);
    font-size: 13px;
    line-height: 1.35;
    font-style: normal;
  }
  .back-brand {
    position: absolute;
    left: 350px;
    top: 70px;
    width: 220px;
    height: 220px;
    display: flex;
    align-items: center;
    justify-content: center;
    text-align: center;
  }
  .back-brand .brand-name { font-size: 26px; }
</style>
</head>
<body>
<main class="canvas">

  <section class="card card-front" aria-label="Card front">
    <div class="front-photo" role="img" aria-label="Steaming coffee cup resting on roasted coffee beans"></div>
    <div class="brand-seal">
      <span class="brand-name">Copperleaf<br>Roasting<br>House</span>
    </div>
  </section>

  <section class="card card-back" aria-label="Card back">
    <h1 class="holder-name">Griff Tallant</h1>

    <ul class="contact-list">
      <li>
        <svg class="contact-icon" viewBox="0 0 24 24" aria-hidden="true">
          <path fill="#ffffff" d="M6.6 10.8c1.4 2.8 3.8 5.1 6.6 6.6l2.2-2.2c.3-.3.7-.4 1-.2 1.1.4 2.3.6 3.6.6.6 0 1 .4 1 1V20c0 .6-.4 1-1 1C10.6 21 3 13.4 3 4c0-.6.4-1 1-1h3.5c.6 0 1 .4 1 1 0 1.3.2 2.5.6 3.6.1.3 0 .7-.2 1z"/>
        </svg>
        <span>0491326085</span>
      </li>
      <li>
        <svg class="contact-icon" viewBox="0 0 24 24" aria-hidden="true">
          <rect x="3" y="3" width="18" height="18" fill="none" stroke="#ffffff" stroke-width="2.5"/>
        </svg>
        <span>@copperleafroastinghouse</span>
      </li>
    </ul>

    <address class="address">
      61 Wexley Crescent<br>
      Pine Hollow and 23 Dorrit Avenue<br>
      Sallowmere
    </address>

    <div class="back-brand">
      <span class="brand-name">Copperleaf<br>Roasting<br>House</span>
    </div>
  </section>

</main>
</body>
</html>
```